Varrow Business Card Design - Professional Flexible and forward thinking. Clean and Easy to follow

Management Consulting Company. I focus on business development and concept and operational review. I need a progressive, simple and professional layout design for the business cards, letterhead and envelops
Professional Flexible and forward thinking. Clean and Easy to follow
Mature Business persons and professionals and Corporations

Target Market(s)

Mature Business persons and professionals and Corporations - Government org.

Industry/Entity Type

Consulting

Contact Information for Business Card

Requirements
Must have
• Marcus Varrow
• President
• Phone - 347.682.1530
• email - Mvarrow@varrowpartners-example.com
• Skype - Marc.varrow
• 2187 Tollbrook Lane
• Suite 12
• Cedarfield, P.A. 11492
• USA
Nice to have
• www.varrowpartners-example.com
Should not have
• N/A

```html
<!DOCTYPE html>
<html lang="en">
<head>
<meta charset="UTF-8">
<title>Varrow Business Card Design</title>
<link rel="stylesheet" href="https://fonts.googleapis.com/css2?family=Arvo:wght@700&family=Ubuntu:wght@400;500&display=swap">
<style>
  :root {
    --stage: #e4e4e6;
    --brand-red: #ec1c24;
    --card-white: #f7f8fa;
    --ink: #141414;
    --paper-white: #ffffff;
    --shadow: rgba(0, 0, 0, 0.18);
  }
  * { box-sizing: border-box; margin: 0; padding: 0; }
  html, body {
    width: 1200px;
    height: 900px;
    overflow: hidden;
    background: var(--stage);
    font-family: "Ubuntu", sans-serif;
  }
  .stage {
    width: 1200px;
    height: 900px;
    display: flex;
    align-items: center;
    justify-content: center;
    gap: 40px;
  }
  .card {
    position: relative;
    width: 540px;
    height: 309px;
    box-shadow: 0 10px 30px var(--shadow);
    overflow: hidden;
  }

  /* Front */
  .card-front { background: var(--brand-red); color: var(--paper-white); }
  .brand-name {
    position: absolute;
    top: 82px;
    left: 0;
    right: 0;
    text-align: center;
    font-family: "Arvo", serif;
    font-weight: 700;
    font-size: 34px;
    letter-spacing: 1px;
    color: var(--paper-white);
  }
  .tagline-row {
    position: absolute;
    left: 34px;
    right: 34px;
    top: 228px;
    display: flex;
    align-items: center;
    gap: 14px;
  }
  .tagline-rule {
    flex: 1;
    height: 2px;
    background: var(--paper-white);
  }
  .tagline {
    font-size: 15px;
    font-weight: 500;
    letter-spacing: 1.2px;
    white-space: nowrap;
  }

  /* Back */
  .card-back { background: var(--card-white); color: var(--ink); }
  .accent-rule {
    position: absolute;
    left: 0;
    top: 72px;
    width: 222px;
    height: 4px;
    background: var(--brand-red);
  }
  .identity {
    position: absolute;
    left: 240px;
    top: 42px;
  }
  .person-name {
    font-family: "Arvo", serif;
    font-weight: 700;
    font-size: 25px;
    line-height: 1;
  }
  .person-name .surname { color: var(--brand-red); }
  .person-title {
    font-size: 15px;
    margin-top: 3px;
  }
  .contact-list {
    position: absolute;
    left: 240px;
    top: 118px;
    list-style: none;
    font-size: 13px;
    line-height: 1.35;
  }
  .contact-item {
    display: flex;
    align-items: flex-start;
    gap: 10px;
  }
  .contact-item + .contact-item { margin-top: 3px; }
  .contact-item.gap-before { margin-top: 14px; }
  .contact-icon {
    width: 14px;
    height: 14px;
    flex: none;
    margin-top: 2px;
  }
  .address-lines { display: block; }
</style>
</head>
<body>
<main class="stage">
  <section class="card card-front" aria-label="Card front">
    <div class="brand-name">Varrow</div>
    <div class="tagline-row">
      <span class="tagline-rule"></span>
      <span class="tagline">Management Consulting Company</span>
      <span class="tagline-rule"></span>
    </div>
  </section>

  <section class="card card-back" aria-label="Card back">
    <span class="accent-rule"></span>
    <div class="identity">
      <h1 class="person-name">Marcus <span class="surname">Varrow</span></h1>
      <p class="person-title">President</p>
    </div>
    <ul class="contact-list">
      <li class="contact-item">
        <svg class="contact-icon" viewBox="0 0 16 16" aria-hidden="true"><path fill="#141414" d="M2 6c0-3 3-4 6-4s6 1 6 4l-3 1-1-2H6L5 7 2 6zm2 2h8l2 6H2l2-6zm4 1.5a2 2 0 1 0 0 4 2 2 0 0 0 0-4z"/></svg>
        <span>347 . 682 . 1530</span>
      </li>
      <li class="contact-item">
        <svg class="contact-icon" viewBox="0 0 16 16" aria-hidden="true"><path fill="#141414" d="M1 3h14v10H1z"/><path fill="none" stroke="#f7f8fa" stroke-width="1.3" d="M1.5 3.8 8 9l6.5-5.2"/></svg>
        <span>Mvarrow@varrowpartners-example.com</span>
      </li>
      <li class="contact-item">
        <svg class="contact-icon" viewBox="0 0 16 16" aria-hidden="true"><circle cx="8" cy="8" r="7" fill="#141414"/></svg>
        <span>Marc.varrow</span>
      </li>
      <li class="contact-item gap-before">
        <svg class="contact-icon" viewBox="0 0 16 16" aria-hidden="true"><g fill="none" stroke="#141414" stroke-width="2" stroke-linecap="round"><path d="M7 9.5 4.5 12a2 2 0 0 1-3-3L4 6.5"/><path d="M9 6.5 11.5 4a2 2 0 0 1 3 3L12 9.5"/><path d="M6 10l4-4"/></g></svg>
        <span>www.varrowpartners-example.com</span>
      </li>
      <li class="contact-item">
        <svg class="contact-icon" viewBox="0 0 16 16" aria-hidden="true"><path fill="#141414" d="M8 1a5 5 0 0 0-5 5c0 4 5 9 5 9s5-5 5-9a5 5 0 0 0-5-5zm0 3a2 2 0 1 1 0 4 2 2 0 0 1 0-4z"/></svg>
        <span class="address-lines">2187 Tollbrook Lane<br>Suite 12<br>Cedarfield, P.A. 11492<br>USA</span>
      </li>
    </ul>
  </section>
</main>
</body>
</html>
```